Use responsive design to make this page look and behave awesome in any size

YOU CAN SUBMIT PSD, HOWEVER, THE WINNER MUST SUBMIT PROVIDE A SINGLE CODED PAGE PER THE LINK AND INSTRUCTIONS AT THE BOTTOM OF THIS BRIEF. While developing an internal website, we realized we are not super great at making things look awesome and responsive for phone/tablet/desktop. Thats where you come in. We want you to take this code, Fork it, and then make it look awesome and work great on any size device.

Task at hand:

This page is a simple dashboard showing how a number of stores stack up against each other and against a corporate goal.

Top: Goal title, and where the logged in person's store stands in the ranking.
Green means you are in compliance
Red means you are not in compliance

Middle: Description of goal. Words to describe what the corporate goal is, and a target number.

Bottom: Here we just want to show the top 10 and bottom 5 out of 100+ stores. if your in the top ten, you are highlighted. If your in the bottom 5, you will be highlighted there too. If you are in the middle, we would put the your store info between the top and bottom... indicating your in the middle.
Green means you they are in compliance
Red means they are not in compliance

Your Mission is not only to make this look fantastic and responsive, but to have usable code in there.

You don't need to do any logic. All we care about is look and feel and responsive behavior on different size browsers.

The winner obviously gets the prize, and hopefully can become a solid resource to do more of this type of thing for us in the future.

Instructions:
Go to this link: https://codequill.example/edit/tvx-leaderpanel-widget
Click on the blue Fork button. This will give you a new URL that you can paste back into the contest to review results for us to see your work.
Uploading pictures is not necessary as the responsive code is what is important here.

Good luck!

Number of Pages Required

1 page

Requirements
Must have
• The page must be responsive and look very professional AND game like.
Should not have
• plugins. just native code

```html
<!DOCTYPE html>
<html lang="en">
<head>
<meta charset="utf-8">
<title>Lead Measures</title>
<link href="https://fonts.googleapis.com/css2?family=Open+Sans:wght@400;600;700&display=swap" rel="stylesheet">
<style>
  :root{
    --brand:#007bff;
    --page:#f6f6f6;
    --card:#ffffff;
    --line:#e3e3e3;
    --ink:#222222;
    --ok:#28a745;
    --bad:#dc3545;
    --white:#ffffff;
  }
  *{box-sizing:border-box;margin:0;padding:0}
  html,body{width:1200px;height:951px;overflow:hidden}
  body{
    font-family:"Open Sans",sans-serif;
    color:var(--ink);
    background:linear-gradient(var(--brand) 0 234px,var(--page) 234px);
    position:relative;
  }
  .page-title{
    position:absolute;top:60px;left:0;right:0;
    text-align:center;color:var(--white);
    font-size:24px;font-weight:600;letter-spacing:.3px;
  }
  .board{
    position:absolute;top:127px;left:30px;
    display:grid;grid-template-columns:repeat(4,267px);gap:24px;align-items:start;
  }
  .measure{background:var(--card);padding-bottom:15px}
  .measure-head{
    height:44px;display:flex;justify-content:center;align-items:center;gap:16px;
    font-size:15.5px;border-bottom:1px solid var(--line);
  }
  .measure-goal{
    height:65px;display:flex;justify-content:space-between;align-items:flex-start;
    padding:17px 16px 0;
  }
  .measure--values .measure-goal{height:80px}
  .goal-text{font-size:11.5px;line-height:15px;width:150px}
  .goal-target{font-size:15px;width:70px;padding-top:0;margin-top:-1px}
  .ranking{list-style:none;margin:0 16px}
  .ranking + .ranking{margin-top:19px}
  .rank-row{
    height:39px;display:flex;align-items:center;
    padding:0 16px;border:1px solid var(--line);margin-top:-1px;
    font-size:12px;
  }
  .rank-row:first-child{margin-top:0}
  .rank-pos{font-weight:700;margin-right:5px}
  .rank-name{flex:1}
  .ok{color:var(--ok)}
  .bad{color:var(--bad)}
  .rank-row--mine{background:var(--bad);border-color:var(--bad);color:var(--white)}
  .rank-row--mine .rank-pos{color:#7a1b24}
</style>
</head>
<body>
<h1 class="page-title">LEAD MEASURES</h1>
<main class="board">

  <section class="measure">
    <header class="measure-head"><span>Team</span><span>92.1%</span></header>
    <div class="measure-goal"><p class="goal-text">Use Slow Stock wherever possible</p><p class="goal-target">80%</p></div>
    <ol class="ranking">
      <li class="rank-row bad"><span class="rank-pos" style="color:var(--ink)">1</span><span class="rank-name">(1) yjcQbtCyQu</span><span>1%</span></li>
      <li class="rank-row bad"><span class="rank-pos" style="color:var(--ink)">2</span><span class="rank-name">(1) crsmicfXwS</span><span>1%</span></li>
      <li class="rank-row bad"><span class="rank-pos" style="color:var(--ink)">3</span><span class="rank-name">(2) wnLJojLRSf</span><span>2%</span></li>
      <li class="rank-row bad"><span class="rank-pos" style="color:var(--ink)">4</span><span class="rank-name">(2) swEbjeRrpi</span><span>2%</span></li>
      <li class="rank-row bad"><span class="rank-pos" style="color:var(--ink)">5</span><span class="rank-name">(4) oUauMPncOA</span><span>4%</span></li>
      <li class="rank-row bad"><span class="rank-pos" style="color:var(--ink)">6</span><span class="rank-name">(5) vYuFdHZExR</span><span>5%</span></li>
      <li class="rank-row bad"><span class="rank-pos" style="color:var(--ink)">7</span><span class="rank-name">(5) jvBnNaGkeE</span><span>5%</span></li>
      <li class="rank-row bad"><span class="rank-pos" style="color:var(--ink)">8</span><span class="rank-name">(6) CuWllvexCs</span><span>6%</span></li>
      <li class="rank-row bad"><span class="rank-pos" style="color:var(--ink)">9</span><span class="rank-name">(7) XQFCUbSoko</span><span>7%</span></li>
      <li class="rank-row bad"><span class="rank-pos" style="color:var(--ink)">10</span><span class="rank-name">(7) GucpFDVVJP</span><span>7%</span></li>
    </ol>
    <ol class="ranking">
      <li class="rank-row ok"><span class="rank-pos" style="color:var(--ink)">96</span><span class="rank-name">(94) VaDGNkvwai</span><span>94%</span></li>
      <li class="rank-row ok"><span class="rank-pos" style="color:var(--ink)">97</span><span class="rank-name">(94) IBjPTiBSIh</span><span>94%</span></li>
      <li class="rank-row ok"><span class="rank-pos" style="color:var(--ink)">98</span><span class="rank-name">(96) iWwFhTvkZb</span><span>96%</span></li>
      <li class="rank-row ok"><span class="rank-pos" style="color:var(--ink)">99</span><span class="rank-name">(96) IzLClRKlLu</span><span>96%</span></li>
      <li class="rank-row ok"><span class="rank-pos" style="color:var(--ink)">100</span><span class="rank-name">(96) pXPrzpcrUY</span><span>96%</span></li>
    </ol>
  </section>

  <section class="measure">
    <header class="measure-head"><span>Slow</span><span>0%</span></header>
    <div class="measure-goal"><p class="goal-text">Less than 0% of inventory slower than 100 days</p><p class="goal-target">&lt; 1%</p></div>
    <ol class="ranking">
      <li class="rank-row ok"><span class="rank-pos" style="color:var(--ink)">1</span><span class="rank-name">(89) NZBGVulmnc</span><span>0%</span></li>
      <li class="rank-row ok"><span class="rank-pos" style="color:var(--ink)">2</span><span class="rank-name">(80) GaccDehKUO</span><span>0%</span></li>
      <li class="rank-row ok"><span class="rank-pos" style="color:var(--ink)">3</span><span class="rank-name">(55) aPfpNcqcDh</span><span>0%</span></li>
      <li class="rank-row ok"><span class="rank-pos" style="color:var(--ink)">4</span><span class="rank-name">(97) YqyVfKlTIl</span><span>0%</span></li>
      <li class="rank-row ok"><span class="rank-pos" style="color:var(--ink)">5</span><span class="rank-name">(67) PvQdqyeaHr</span><span>0%</span></li>
      <li class="rank-row rank-row--mine"><span class="rank-pos">6</span><span class="rank-name">(00) Your Store</span><span>2%</span></li>
      <li class="rank-row bad"><span class="rank-pos" style="color:var(--ink)">7</span><span class="rank-name">(40) jyMfVYIVbl</span><span>2%</span></li>
      <li class="rank-row bad"><span class="rank-pos" style="color:var(--ink)">8</span><span class="rank-name">(11) QSESmpDJqw</span><span>2%</span></li>
      <li class="rank-row bad"><span class="rank-pos" style="color:var(--ink)">9</span><span class="rank-name">(71) nIlaXFpJWv</span><span>2%</span></li>
      <li class="rank-row bad"><span class="rank-pos" style="color:var(--ink)">10</span><span class="rank-name">(51) ENrkkveKpb</span><span>2%</span></li>
    </ol>
    <ol class="ranking">
      <li class="rank-row bad"><span class="rank-pos" style="color:var(--ink)">96</span><span class="rank-name">(90) VZgTUWgJTU</span><span>8%</span></li>
      <li class="rank-row bad"><span class="rank-pos" style="color:var(--ink)">97</span><span class="rank-name">(67) nRGVsKcZhP</span><span>9%</span></li>
      <li class="rank-row bad"><span class="rank-pos" style="color:var(--ink)">98</span><span class="rank-name">(32) JckeFPUVJV</span><span>9%</span></li>
      <li class="rank-row bad"><span class="rank-pos" style="color:var(--ink)">99</span><span class="rank-name">(57) RxygcFNCRC</span><span>9%</span></li>
      <li class="rank-row bad"><span class="rank-pos" style="color:var(--ink)">100</span><span class="rank-name">(20) MmydxeaOMu</span><span>10%</span></li>
    </ol>
  </section>

  <section class="measure">
    <header class="measure-head"><span>Turns</span><span>2.2</span></header>
    <div class="measure-goal"><p class="goal-text">Turn inventory 6 or more times a year</p><p class="goal-target">&gt; 6</p></div>
    <ol class="ranking">
      <li class="rank-row bad"><span class="rank-pos" style="color:var(--ink)">1</span><span class="rank-name">(8) VZaEOSVkef</span><span>0.2</span></li>
      <li class="rank-row bad"><span class="rank-pos" style="color:var(--ink)">2</span><span class="rank-name">(3) PcVKNpUNmj</span><span>0.2</span></li>
      <li class="rank-row bad"><span class="rank-pos" style="color:var(--ink)">3</span><span class="rank-name">(4) RIlyRZsTIn</span><span>0.4</span></li>
      <li class="rank-row bad"><span class="rank-pos" style="color:var(--ink)">4</span><span class="rank-name">(9) epiNQFtERO</span><span>0.6</span></li>
      <li class="rank-row bad"><span class="rank-pos" style="color:var(--ink)">5</span><span class="rank-name">(3) FbFOzkjSpF</span><span>0.7</span></li>
      <li class="rank-row bad"><span class="rank-pos" style="color:var(--ink)">6</span><span class="rank-name">(7) RdzzkcVqtC</span><span>0.8</span></li>
      <li class="rank-row bad"><span class="rank-pos" style="color:var(--ink)">7</span><span class="rank-name">(1) DiilXiGkTx</span><span>0.8</span></li>
      <li class="rank-row bad"><span class="rank-pos" style="color:var(--ink)">8</span><span class="rank-name">(1) jxWbwORyVa</span><span>0.8</span></li>
      <li class="rank-row bad"><span class="rank-pos" style="color:var(--ink)">9</span><span class="rank-name">(4) UyzYfiIMzU</span><span>0.8</span></li>
      <li class="rank-row bad"><span class="rank-pos" style="color:var(--ink)">10</span><span class="rank-name">(4) KVIgJQBgAc</span><span>1</span></li>
    </ol>
    <ol class="ranking">
      <li class="rank-row ok"><span class="rank-pos" style="color:var(--ink)">96</span><span class="rank-name">(5) gBeGhPqZNF</span><span>9.7</span></li>
      <li class="rank-row ok"><span class="rank-pos" style="color:var(--ink)">97</span><span class="rank-name">(8) gGhhZFlCHP</span><span>9.7</span></li>
      <li class="rank-row ok"><span class="rank-pos" style="color:var(--ink)">98</span><span class="rank-name">(9) emavLKfhzN</span><span>9.8</span></li>
      <li class="rank-row ok"><span class="rank-pos" style="color:var(--ink)">99</span><span class="rank-name">(7) PyuviZHBxH</span><span>9.8</span></li>
      <li class="rank-row ok"><span class="rank-pos" style="color:var(--ink)">100</span><span class="rank-name">(5) LldsyctcWm</span><span>9.9</span></li>
    </ol>
  </section>

  <section class="measure measure--values">
    <header class="measure-head"><span>Values</span><span>1.9</span></header>
    <div class="measure-goal"><p class="goal-text">Inventory Value to be around 1.25 x you last months INVENTORY sales</p><p class="goal-target">1.25</p></div>
    <ol class="ranking">
      <li class="rank-row ok"><span class="rank-pos" style="color:var(--ink)">1</span><span class="rank-name">(8) VZaEOSVkef</span><span>0.2</span></li>
      <li class="rank-row ok"><span class="rank-pos" style="color:var(--ink)">2</span><span class="rank-name">(3) PcVKNpUNmj</span><span>0.2</span></li>
      <li class="rank-row ok"><span class="rank-pos" style="color:var(--ink)">3</span><span class="rank-name">(4) RIlyRZsTIn</span><span>0.4</span></li>
      <li class="rank-row ok"><span class="rank-pos" style="color:var(--ink)">4</span><span class="rank-name">(9) epiNQFtERO</span><span>0.6</span></li>
      <li class="rank-row ok"><span class="rank-pos" style="color:var(--ink)">5</span><span class="rank-name">(3) FbFOzkjSpF</span><span>0.7</span></li>
      <li class="rank-row ok"><span class="rank-pos" style="color:var(--ink)">6</span><span class="rank-name">(7) RdzzkcVqtC</span><span>0.8</span></li>
      <li class="rank-row ok"><span class="rank-pos" style="color:var(--ink)">7</span><span class="rank-name">(1) DiilXiGkTx</span><span>0.8</span></li>
      <li class="rank-row ok"><span class="rank-pos" style="color:var(--ink)">8</span><span class="rank-name">(1) jxWbwORyVa</span><span>0.8</span></li>
      <li class="rank-row ok"><span class="rank-pos" style="color:var(--ink)">9</span><span class="rank-name">(4) UyzYfiIMzU</span><span>0.8</span></li>
      <li class="rank-row ok"><span class="rank-pos" style="color:var(--ink)">10</span><span class="rank-name">(7) SCXulMdjcB</span><span>1</span></li>
    </ol>
    <ol class="ranking">
      <li class="rank-row bad"><span class="rank-pos" style="color:var(--ink)">96</span><span class="rank-name">(5) gBeGhPqZNF</span><span>9.7</span></li>
      <li class="rank-row bad"><span class="rank-pos" style="color:var(--ink)">97</span><span class="rank-name">(8) gGhhZFlCHP</span><span>9.7</span></li>
      <li class="rank-row bad"><span class="rank-pos" style="color:var(--ink)">98</span><span class="rank-name">(9) emavLKfhzN</span><span>9.8</span></li>
      <li class="rank-row bad"><span class="rank-pos" style="color:var(--ink)">99</span><span class="rank-name">(7) PyuviZHBxH</span><span>9.8</span></li>
      <li class="rank-row bad"><span class="rank-pos" style="color:var(--ink)">100</span><span class="rank-name">(5) LldsyctcWm</span><span>9.9</span></li>
    </ol>
  </section>

</main>
</body>
</html>
```